Wendlemoor Vapes labels

We need a label designed for our e-liquid that we will be selling from our store. (E-liquid is used in electronic cigarettes) The label should be 1-1.5 inches tall and ~3 inches long.

Try to focus on highlighting the name brand over the specific flavor.

Bottle size will be 15ml clear bottles.

There will be 10+ flavors and each flavor will need a slightly different label (with the same overall theme) and different nicotine levels varying from 0mg, 6mg, 12mg, and 18mg.

Initial favor list is:
Coral Drift
Velvet Slosh
Tart Currants
Crakle Plums
Papaya Riot
Zingy Drops
Amber Gryphon
Fizzleleaf
Emberlash
Orvin
Nutmeg Twist

Please add the following warning in caps and small font:

(WHITE FONT)
This product contains nicotine or was produced at a facility that processes nicotine which has been known to cause birth defects and other reproductive harm. This product also contains VG/PG and artificial flavors. Not for sale to minors.
(RED FONT)
Toxic if swallowed or has contact with skin. Keep locked up and out of reach of children and pets. In case of accident or you feel unwell seek medical advice immediately.

young adults

Electronic

```html
<!DOCTYPE html>
<html lang="en">
<head>
<meta charset="utf-8">
<title>Wendlemoor Vapes label</title>
<link rel="stylesheet" href="https://fonts.googleapis.com/css2?family=Tinos:wght@400;700&display=swap">
<style>
  :root {
    --backdrop: #17110d;
    --label-paper: #ebf0f0;
    --label-blue: #1e5fa2;
    --brand-blue: #0b4fd0;
    --list-blue: #1a5a9e;
    --warning-red: #e30613;
    --warning-white: #ffffff;
  }
  html, body {
    margin: 0;
    padding: 0;
    width: 1200px;
    height: 1000px;
    overflow: hidden;
    background: var(--backdrop);
    font-family: "Tinos", "Times New Roman", serif;
  }
  .label {
    position: absolute;
    left: 150px;
    top: 275px;
    width: 900px;
    height: 450px;
    background: var(--label-paper);
    overflow: hidden;
  }
  .label-wave {
    position: absolute;
    inset: 0;
    width: 900px;
    height: 450px;
  }
  .label-wave path { fill: var(--label-blue); }
  .warning-red {
    position: absolute;
    left: 10px;
    top: 62px;
    width: 240px;
    margin: 0;
    color: var(--warning-red);
    font-size: 10.5px;
    font-weight: 700;
    line-height: 12.5px;
    text-align: center;
  }
  .warning-red-side {
    position: absolute;
    left: 535px;
    top: 140px;
    width: 290px;
    margin: 0;
    color: var(--warning-red);
    font-size: 7px;
    font-style: italic;
    font-weight: 700;
    line-height: 8px;
    text-align: center;
    transform: rotate(-90deg);
    transform-origin: center;
  }
  .brand-name {
    position: absolute;
    left: 250px;
    top: 225px;
    width: 400px;
    margin: 0;
    color: var(--brand-blue);
    font-size: 40px;
    font-weight: 700;
    text-align: center;
    line-height: 48px;
  }
  .brand-dot {
    position: absolute;
    left: 425px;
    top: 50px;
    width: 150px;
    height: 150px;
    border-radius: 50%;
    background: var(--brand-blue);
  }
  .flavour-heading {
    position: absolute;
    left: 721px;
    top: 50px;
    margin: 0;
    color: var(--list-blue);
    font-size: 16px;
    font-weight: 400;
  }
  .flavour-list {
    position: absolute;
    left: 724px;
    top: 73px;
    margin: 0;
    padding: 0;
    list-style: none;
    color: var(--list-blue);
    font-size: 11px;
    font-weight: 700;
    line-height: 16px;
  }
  .bottle-size {
    position: absolute;
    left: 725px;
    top: 295px;
    margin: 0;
    color: var(--warning-white);
    font-size: 14px;
  }
  .warning-white {
    position: absolute;
    left: 35px;
    top: 342px;
    width: 210px;
    margin: 0;
    color: var(--warning-white);
    font-size: 10.5px;
    font-weight: 700;
    line-height: 12.5px;
    letter-spacing: 0.3px;
  }
  .nicotine-levels {
    position: absolute;
    left: 320px;
    top: 370px;
    width: 260px;
    margin: 0;
    color: var(--warning-white);
    font-size: 12px;
    font-weight: 700;
    line-height: 15px;
    letter-spacing: 0.3px;
    text-align: center;
  }
</style>
</head>
<body>
  <section class="label">
    <svg class="label-wave" viewBox="0 0 900 450" aria-hidden="true">
      <path d="M0,250 C150,335 330,365 520,340 C690,318 800,255 900,262 L900,450 L0,450 Z"/>
    </svg>

    <p class="warning-red">Toxic if swallowed or has contact with skin.<br>Keep locked up and out of reach of children and pets.<br>In case of accident or you feel<br>unwell seek medical advice immediately.</p>

    <p class="warning-red-side">Toxic if swallowed or has contact with skin. Keep locked up and out of reach of children and pets.</p>

    <div class="brand-dot"></div>
    <h1 class="brand-name">Wendlemoor Vapes</h1>

    <h2 class="flavour-heading">Initial favor list is:</h2>
    <ul class="flavour-list">
      <li>Coral Drift</li>
      <li>Velvet Slosh</li>
      <li>Tart Currants</li>
      <li>Crakle Plums</li>
      <li>Papaya Riot</li>
      <li>Zingy Drops</li>
      <li>Amber Gryphon</li>
      <li>Fizzleleaf</li>
      <li>Emberlash</li>
      <li>Orvin</li>
      <li>Nutmeg Twist</li>
    </ul>

    <p class="bottle-size">size will be 15ml</p>

    <p class="warning-white">This product contains nicotine or was produced at a facility that processes nicotine which has been known to cause birth defects and other reproductive harm.<br>This product also contains VG/PG and artificial flavors.<br>Not for sale to minors.</p>

    <p class="nicotine-levels">Different nicotine levels varying from<br>0mg, 6mg, 12mg, and 18mg.</p>
  </section>
</body>
</html>
```